Marwick Ostrand Law website for a law firm

modern clean website for a small boutique law firm. Based in Sacramento, CA and the Bay Area. Practice areas of Family Law, Civil litigation, and Criminal Defense. We already have a logo design as well as attorney pictures to include on page.
Would like images of California included on site.
Would like site to go with Logo that is already designed...blue/grey/white colors.

Industry/Entity Type

Law Firm

Number of Pages Required

5+ page

Requirements
Must have
• I already have several pages of content drafted. Just need the pages with images to input content. Must be clean and modern feel. Want it to reflect California and small boutique feel that is provided personalized legal attention.
• Must have a page where I can blog or post articles on.

```html
<!DOCTYPE html>
<html lang="en">
<head>
<meta charset="utf-8">
<title>Marwick Ostrand Law</title>
<link href="https://fonts.googleapis.com/css2?family=Roboto:wght@300;400;500;700;900&family=Roboto+Condensed:wght@700&display=swap" rel="stylesheet">
<style>
:root{
  --blue:#3a7fc9;
  --blue-dark:#2f6cae;
  --orange:#e39b0e;
  --ink:#222;
  --text:#555;
  --muted:#8a8a8a;
  --grey:#8e8e8e;
  --light:#f4f4f4;
  --line:#dcdcdc;
  --dark:#1c1c1c;
  --white:#fff;
}
*{box-sizing:border-box;margin:0;padding:0}
html,body{width:1200px;height:3750px;overflow:hidden}
body{font-family:"Roboto",Arial,sans-serif;color:var(--text);background:var(--white);position:relative}
.abs{position:absolute}
.top-bar{top:0;left:0;width:1200px;height:30px;border-bottom:1px solid #eee;font-size:11px;color:var(--muted)}
.top-bar .info{left:162px;top:9px}
.top-bar .info span{margin-right:28px}
.btn-consult-top{left:905px;top:3px;width:132px;height:23px;background:var(--blue);color:#fff;font-size:11px;line-height:23px;text-align:center}
.site-header{top:30px;left:0;width:1200px;height:75px}
.brand{left:160px;top:24px;display:flex;align-items:center;gap:10px;font-size:24px;font-weight:500;color:var(--blue);line-height:28px;white-space:nowrap}
.brand .mark{width:22px;height:22px;background:var(--blue);flex:none}
.nav{right:162px;top:30px;display:flex;gap:38px;font-size:12px;color:#444;font-weight:500}
.hero{top:105px;left:0;width:1200px;height:520px;background:linear-gradient(100deg,#c9b79a 0%,#7b6a58 35%,#3d3f48 55%,#8c7d70 80%,#d8cfc4 100%)}
.hero-title{right:60px;top:283px;text-align:right;color:#fff}
.hero-title h1{font-family:"Roboto Condensed",sans-serif;font-size:32px;letter-spacing:.5px;white-space:nowrap}
.hero-title p{font-size:11px;font-weight:700;margin-top:2px}
.tab-need{left:162px;top:530px;width:225px;height:45px;background:var(--orange);color:#fff;font-weight:700;font-size:15px;line-height:45px;text-align:center}
.lead-form{left:162px;top:575px;width:875px;height:87px;background:var(--blue);display:flex;align-items:center;padding:0 12px}
.lead-form .field{width:184px;height:32px;background:#fff;border-right:1px solid #ddd;font-size:10px;color:#777;padding:10px 12px}
.lead-form .submit{margin-left:12px;width:100px;height:36px;background:#111;color:#fff;font-size:12px;font-weight:700;text-align:center;line-height:36px}
.sec-title{border-left:5px solid var(--blue);padding-left:14px;font-size:28px;font-weight:700;color:var(--ink);line-height:32px;white-space:nowrap}
.welcome-title{left:162px;top:700px}
.welcome-intro{left:178px;top:740px;width:400px;font-size:10.5px;line-height:15px}
.feature{width:420px;display:flex;gap:18px}
.feature .ic{width:50px;height:50px;border:1px solid #bbb;border-radius:50%;flex:none;display:flex;align-items:center;justify-content:center}
.feature h3{font-size:17px;font-weight:500;color:var(--ink);margin-bottom:6px}
.feature p{font-size:11px;line-height:15px}
.founders{left:612px;top:712px;width:425px;height:330px;background:#a9a9a9;padding:8px}
.founders .img{width:409px;height:262px;background:linear-gradient(90deg,#9a5d46,#c7977a 55%,#8c8c8c)}
.founders p{color:#fff;font-size:14px;margin-top:22px;padding-left:8px;white-space:nowrap}
.services{top:1095px;left:0;width:1200px;height:335px;background:linear-gradient(90deg,#9a9a9a,#7c7c7c 50%,#929292)}
.services .label{left:160px;top:45px;color:#fff}
.services .label small{display:block;font-size:22px;font-weight:700}
.services .label b{font-size:40px;font-weight:500;display:block;line-height:40px}
.services .rule{left:160px;top:135px;width:200px;height:1px;background:rgba(255,255,255,.6)}
.services .copy{left:160px;top:150px;width:340px;font-size:10px;line-height:14px;color:#fff}
.services .copy p+p{margin-top:14px}
.btn-dark{background:#1a1a1a;color:#fff;font-size:11px;text-align:center}
.services .more{left:160px;top:262px;width:130px;height:30px;line-height:30px}
.tile{width:235px;height:132px}
.tile .img{height:132px}
.tile .cap{height:22px;margin-top:-22px;position:relative;background:rgba(40,40,40,.75);color:#fff;font-size:12px;font-weight:700;text-align:center;line-height:22px}
.quote{top:1430px;left:0;width:1200px;height:195px;background:linear-gradient(180deg,#4a8ad0,#3a79bf)}
.q-field{width:192px;height:32px;background:#fff;font-size:10px;color:#777;padding:10px 10px;white-space:nowrap;overflow:hidden}
.quote .cta{left:162px;top:130px;width:188px;height:32px;background:var(--orange);color:#fff;font-size:11px;font-weight:700;text-align:center;line-height:32px}
.quote .head{right:165px;top:95px;color:#fff;text-align:right}
.quote .head small{font-size:14px;font-weight:700;display:block}
.quote .head b{font-size:40px;font-weight:700;line-height:40px}
.why-photo{left:150px;top:1655px;width:375px;height:440px;background:linear-gradient(180deg,#ddd3c8,#3a3030 60%,#1e1b1b)}
.why-title{left:612px;top:1695px}
.why-intro{left:628px;top:1735px;width:410px;font-size:11px;line-height:15px}
.stats{top:2095px;left:0;width:1200px;height:200px;background:linear-gradient(90deg,#d7920c,#e8a51a 50%,#d7920c)}
.stat{top:57px;width:200px;text-align:center;color:#fff}
.stat b{display:block;font-size:52px;font-weight:700;line-height:56px}
.stat span{font-size:10px;font-weight:500}
.center-title{left:0;width:1200px;text-align:center;font-size:26px;font-weight:700;color:var(--ink)}
.center-title::after{content:"";display:block;width:40px;height:3px;background:var(--blue);margin:8px auto 0}
.att-card{top:2425px;width:425px;height:225px;background:var(--light);padding:25px 22px;display:flex;gap:22px}
.att-card .img{width:168px;height:185px;flex:none}
.att-card h3{font-size:19px;font-weight:700;color:var(--ink);margin-bottom:10px;white-space:nowrap}
.att-card p{font-size:11px;line-height:15px;margin-bottom:10px}
.read{display:inline-block;border:1px solid #333;font-size:9px;padding:4px 8px;color:#333;white-space:nowrap}
.socials-sm{display:inline-flex;gap:8px;margin-left:24px;vertical-align:middle}
.socials-sm i{width:13px;height:13px;background:#999;display:block}
.blog-main{left:162px;top:2770px;width:425px;height:292px;background:linear-gradient(90deg,#6b4b34,#caa687 45%,#4c3a2d)}
.date{position:absolute;left:0;bottom:0;width:45px;height:45px;background:var(--blue);color:#fff;text-align:center;font-size:13px;font-weight:700;padding-top:7px;line-height:15px}
.date small{display:block;font-size:10px}
.blog-item{left:612px;width:425px;height:145px}
.blog-item .img{position:absolute;left:0;top:0;width:135px;height:145px;background:linear-gradient(135deg,#5a3d2b,#b48868 60%,#6d4a34)}
.blog-item .txt{position:absolute;left:145px;top:0;width:280px}
.blog-item h4{font-size:12px;font-weight:700;color:var(--ink);margin-bottom:5px}
.blog-item .meta{font-size:9px;color:var(--muted);margin-bottom:5px}
.blog-item .meta b{color:var(--ink)}
.blog-item p{font-size:10px;line-height:14px}
.blog-item .row{display:flex;align-items:center;margin-top:10px;font-size:9px;white-space:nowrap}
.blog-item .row .read{border-color:var(--blue);color:#333}
.consult{top:3150px;left:0;width:1200px;height:262px;background:linear-gradient(90deg,#3a7fc9,#4c8dd4 50%,#3a7fc9)}
.consult .txt{left:168px;top:58px;color:#fff}
.consult h2{font-size:20px;font-weight:700}
.consult p{font-size:11px;font-weight:500;margin-top:4px}
.consult .btn{left:775px;top:58px;width:272px;height:48px;background:#111;color:#fff;font-size:16px;font-weight:700;text-align:center;line-height:48px}
.footer{top:3412px;left:0;width:1200px;height:338px;background:var(--dark)}
.newsletter{left:170px;top:3325px;width:875px;height:175px;background:var(--orange);text-align:center;color:#fff;padding-top:22px}
.newsletter h2{font-size:28px;font-weight:500;letter-spacing:.5px}
.newsletter p{font-size:11px;margin-top:2px}
.newsletter .form{display:flex;justify-content:center;margin-top:20px}
.newsletter .in{width:355px;height:40px;background:#fff;font-size:10px;color:#888;text-align:left;padding:14px}
.newsletter .go{width:110px;height:40px;background:#1a1a1a;font-size:14px;line-height:40px}
.join{top:3520px;left:0;width:1200px;text-align:center;color:#fff;font-size:34px;font-weight:500}
.soc{top:3590px;left:0;width:1200px;display:flex;justify-content:center;gap:16px}
.soc i{width:34px;height:34px;border:1px solid #888;border-radius:50%;display:block}
.foot-nav{top:3677px;left:0;width:1200px;display:flex;justify-content:center;gap:32px;font-size:10px;color:#aaa}
.copy-line{top:3712px;left:0;width:1200px;text-align:center;font-size:9px;color:#777}
</style>
</head>
<body>

<div class="abs top-bar">
  <div class="abs info"><span>&#9679; Mon - Sat 7:00 - 17:00</span><span>&#9742; 555-210-4480</span></div>
  <div class="abs btn-consult-top">Get Free Consultation</div>
</div>

<header class="abs site-header">
  <div class="abs brand"><span class="mark"></span>Marwick Ostrand Law</div>
  <nav class="abs nav"><span>HOME</span><span>ABOUT US</span><span>PRACTICE AREAS</span><span>CONTACT US</span></nav>
</header>

<section class="abs hero" role="img" aria-label="Photo of the firm's attorneys standing together in an office"></section>
<div class="abs hero-title"><h1>MARWICK &amp; OSTRAND LAW</h1><p>STRONG REPUTATIONS DON'T GO UNNOTICED</p></div>
<div class="abs tab-need">NEED A LEGAL ASSISTANT</div>
<form class="abs lead-form">
  <div class="field">NAME*</div><div class="field">EMAIL*</div><div class="field">PHONE*</div><div class="field">CITY*</div>
  <div class="submit">SUBMIT NOW</div>
</form>

<h2 class="abs sec-title welcome-title">WELCOME TO MOLAW</h2>
<p class="abs welcome-intro">After practicing in both the private and public sector for several years, Clara Marwick and Evan Ostrand joined their legal expertise and formed Marwick &amp; Ostrand Law in 2016. With a combined 15 years of experience, Clara and Evan focus on Civil Litigation, Family Law, Immigration and Criminal Defense. Their goal is to give every client the best possible outcome in each and every case.</p>

<div class="abs feature" style="left:178px;top:838px">
  <div class="ic"><svg width="22" height="22" viewBox="0 0 22 22"><circle cx="9" cy="9" r="6.5" fill="none" stroke="#333" stroke-width="2"/><line x1="14" y1="14" x2="20" y2="20" stroke="#333" stroke-width="2.5"/></svg></div>
  <div><h3>Investigation</h3><p>Lorem Ipsum is simply dummy text of the printing and typesetting industry. Lorem Ipsum has been the industry's standard dummy text</p></div>
</div>
<div class="abs feature" style="left:178px;top:918px">
  <div class="ic"><svg width="24" height="22" viewBox="0 0 24 22"><rect x="6" y="2" width="10" height="5" transform="rotate(-30 11 4.5)" fill="#333"/><line x1="11" y1="6" x2="19" y2="14" stroke="#333" stroke-width="2.5"/><rect x="2" y="17" width="12" height="3" fill="#333"/></svg></div>
  <div><h3>Legal Proceeding</h3><p>Lorem Ipsum is simply dummy text of the printing and typesetting industry. Lorem Ipsum has been the industry's standard dummy text</p></div>
</div>
<div class="abs feature" style="left:178px;top:998px">
  <div class="ic"><svg width="24" height="22" viewBox="0 0 24 22"><line x1="12" y1="2" x2="12" y2="19" stroke="#333" stroke-width="2"/><line x1="3" y1="5" x2="21" y2="5" stroke="#333" stroke-width="2"/><path d="M1 12 L4 5 L7 12 Z M17 12 L20 5 L23 12 Z" fill="none" stroke="#333" stroke-width="1.5"/><rect x="7" y="19" width="10" height="2" fill="#333"/></svg></div>
  <div><h3>Fight for Justice</h3><p>Lorem Ipsum is simply dummy text of the printing and typesetting industry. Lorem Ipsum has been the industry's standard dummy text</p></div>
</div>

<figure class="abs founders">
  <div class="img" role="img" aria-label="Photo of the two founding partners in front of a brick wall"></div>
  <p>FOUNDING PARTNERS, EVAN OSTRAND &amp; CLARA MARWICK</p>
</figure>

<section class="abs services" role="img" aria-label="Faded photo of a lawyer at a desk">
  <div class="abs label"><small>VIEW OUR</small><b>SERVICES</b></div>
  <div class="abs rule"></div>
  <div class="abs copy">
    <p>Lorem ipsum dolor sit amet, consectetur adipiscing elit. Donec dapibus odio vel tellus finibus placerat. In vel purus sed lacus sodales venenatis. Integer id convallis nulla, in fringilla.</p>
    <p>Mauris ut mi leo. Fusce vehicula nisl sed vulputate convallis. Integer consequat, enim eu tempor vulputate, libero arcu luctus libero, sit amet pretium enim est eget est. Phasellus.</p>
  </div>
  <div class="abs btn-dark more">READ MORE &#8250;</div>
  <div class="abs tile" style="left:562px;top:30px"><div class="img" role="img" aria-label="Photo of law books on a shelf" style="background:linear-gradient(135deg,#4a2a18,#9c5a30 50%,#3a2014)"></div><div class="cap">CIVIL LITIGATION</div></div>
  <div class="abs tile" style="left:802px;top:30px"><div class="img" role="img" aria-label="Photo of a hand signing a document" style="background:linear-gradient(135deg,#e8e4df,#bdb4aa)"></div><div class="cap">FAMILY LAW</div></div>
  <div class="abs tile" style="left:562px;top:170px"><div class="img" role="img" aria-label="Photo of a conference table" style="background:linear-gradient(135deg,#3a3532,#8a6a4e 55%,#4b3f37)"></div><div class="cap">IMMIGRATION</div></div>
  <div class="abs tile" style="left:802px;top:170px"><div class="img" role="img" aria-label="Photo of scales of justice" style="background:linear-gradient(135deg,#6b3a1e,#c07a3e 55%,#5a2f18)"></div><div class="cap">CRIMINAL DEFENSE</div></div>
</section>

<section class="abs quote" role="img" aria-label="Blue tinted California city skyline">
  <div class="abs q-field" style="left:162px;top:45px">Name / Company Name</div>
  <div class="abs q-field" style="left:362px;top:45px">Email</div>
  <div class="abs q-field" style="left:562px;top:45px">Phone Number</div>
  <div class="abs q-field" style="left:162px;top:85px">Number Of Case</div>
  <div class="abs q-field" style="left:362px;top:85px">Number Of Outgoing Invoices</div>
  <div class="abs q-field" style="left:562px;top:85px">Number Of Incoming Invoices</div>
  <div class="abs cta">GET A FREE QUOTE &#8594;</div>
  <svg class="abs" style="right:170px;top:30px" width="56" height="50" viewBox="0 0 56 50"><path d="M4 0h20v22c0 14-8 24-20 28l-3-6c7-3 11-9 11-16H4z M32 0h20v22c0 14-8 24-20 28l-3-6c7-3 11-9 11-16h-8z" fill="#fff"/></svg>
  <div class="abs head"><small>GET A FREE QUOTE</small><b>OUR SERVICES</b></div>
</section>

<div class="abs why-photo" role="img" aria-label="Photo of an attorney in a courtroom robe holding a book"></div>
<h2 class="abs sec-title why-title">WHY CHOOSE MOLAW</h2>
<p class="abs why-intro">Lorem Ipsum is simply dummy text of the printing and typesetting industry. Lorem Ipsum has been the industry's standard dummy text ever since the 1500s, when an unknown printer took a galley of type and scrambled it to make a type specimen book.</p>

<div class="abs feature" style="left:628px;top:1820px">
  <div class="ic"><svg width="26" height="22" viewBox="0 0 26 22"><circle cx="13" cy="5" r="3.5" fill="#333"/><circle cx="5" cy="8" r="2.5" fill="#333"/><circle cx="21" cy="8" r="2.5" fill="#333"/><path d="M8 20v-6a5 5 0 0 1 10 0v6z M1 20v-4a4 4 0 0 1 6-3v7z M25 20v-4a4 4 0 0 0-6-3v7z" fill="#333"/></svg></div>
  <div><h3>We have best Attorneys team</h3><p>Lorem Ipsum is simply dummy text of the printing and typesetting industry. Lorem Ipsum has been the industry's standard dummy text</p></div>
</div>
<div class="abs feature" style="left:628px;top:1897px">
  <div class="ic"><svg width="22" height="20" viewBox="0 0 22 20"><rect x="1" y="5" width="20" height="14" rx="2" fill="#333"/><rect x="7" y="1" width="8" height="5" fill="none" stroke="#333" stroke-width="2"/></svg></div>
  <div><h3>Best Case Strategy</h3><p>Lorem Ipsum is simply dummy text of the printing and typesetting industry. Lorem Ipsum has been the industry's standard dummy text</p></div>
</div>
<div class="abs feature" style="left:628px;top:1975px">
  <div class="ic"><svg width="22" height="20" viewBox="0 0 22 20"><rect x="2" y="2" width="18" height="4" fill="#333"/><rect x="2" y="8" width="18" height="4" fill="#333"/><rect x="2" y="14" width="18" height="4" fill="#333"/></svg></div>
  <div><h3>Review your Case Documents</h3><p>Lorem Ipsum is simply dummy text of the printing and typesetting industry. Lorem Ipsum has been the industry's standard dummy text</p></div>
</div>

<section class="abs stats" role="img" aria-label="Orange tinted city skyline">
  <div class="abs stat" style="left:162px"><b>4025</b><span>SUCCESSFUL CASES</span></div>
  <div class="abs stat" style="left:382px"><b>3270</b><span>TRUSTED CLIENTS</span></div>
  <div class="abs stat" style="left:605px"><b>6349</b><span>CASE STUDIES</span></div>
  <div class="abs stat" style="left:832px"><b>851</b><span>RECIEVED CASE</span></div>
</section>

<h2 class="abs center-title" style="top:2340px">OUR ATTORNEYS</h2>
<article class="abs att-card" style="left:162px">
  <div class="img" role="img" aria-label="Portrait of attorney Clara T. Marwick" style="background:linear-gradient(180deg,#7a5a4a,#3a2a24)"></div>
  <div><h3>Clara T. Marwick</h3><p>Clara Marwick founder and partner, is a California native who grew up in the same community she serves.</p><p>A former prosecutor, Clara has decided to start her private practice to focus more attention on individual clients.</p><span class="read">READ MORE &#10140;</span><span class="socials-sm"><i></i><i></i><i></i></span></div>
</article>
<article class="abs att-card" style="left:612px">
  <div class="img" role="img" aria-label="Portrait of attorney Evan Ostrand" style="background:linear-gradient(180deg,#8a7a6a,#2a2a30)"></div>
  <div><h3>Evan Ostrand</h3><p>Evan Ostrand founder and partner, is a California native who grew up in the same community he serves.</p><p>A former prosecutor, Evan has decided to start his private practice to focus more attention on individual clients.</p><span class="read">READ MORE &#10140;</span><span class="socials-sm"><i></i><i></i><i></i></span></div>
</article>

<h2 class="abs center-title" style="top:2697px">LATEST BLOG</h2>
<div class="abs blog-main" role="img" aria-label="Photo of a lawyer in a law library"><div class="date">15<small>DEC</small></div></div>
<article class="abs blog-item" style="top:2770px">
  <div class="img" role="img" aria-label="Photo of scales of justice"><div class="date">15<small>DEC</small></div></div>
  <div class="txt"><h4>BLOG HEADING HERE</h4><div class="meta">Posted by: <b>Anna Reyes</b> on April 5th,2017</div><p>Lorem Ipsum is simply dummy text of the printing and typesetting industry. Lorem Ipsum has been the industry</p>
  <div class="row"><span class="read">READ MORE &#10140;</span><span style="margin-left:auto;color:var(--blue)">&#9679;</span>&nbsp;Comments&nbsp;&nbsp;<span style="color:var(--blue)">&#9829;</span>&nbsp;5 Likes</div></div>
</article>
<div class="abs" style="left:612px;top:2930px;width:425px;height:1px;background:var(--line)"></div>
<article class="abs blog-item" style="top:2945px">
  <div class="img" role="img" aria-label="Photo of scales of justice"><div class="date">15<small>DEC</small></div></div>
  <div class="txt"><h4>BLOG HEADING HERE</h4><div class="meta">Posted by: <b>Anna Reyes</b> on April 5th,2017</div><p>Lorem Ipsum is simply dummy text of the printing and typesetting industry. Lorem Ipsum has been the industry</p>
  <div class="row"><span class="read">READ MORE &#10140;</span><span style="margin-left:auto;color:var(--blue)">&#9679;</span>&nbsp;Comments&nbsp;&nbsp;<span style="color:var(--blue)">&#9829;</span>&nbsp;5 Likes</div></div>
</article>

<section class="abs consult" role="img" aria-label="Blue tinted photo of a handshake">
  <div class="abs txt"><h2>CONSULTING SERVICE</h2><p>Lorem Ipsum is simply dummy text of the printing and typesetting industry Lorem Ipsum.</p></div>
  <div class="abs btn">GET FREE CONSULTATION &#8250;</div>
</section>

<footer class="abs footer"></footer>
<section class="abs newsletter">
  <h2>NEWSLETTER</h2>
  <p>Enter your email address for getting updates</p>
  <div class="form"><div class="in">Enter your email id</div><div class="go">Subscribe</div></div>
</section>
<div class="abs join">Join the conversation</div>
<div class="abs soc"><i></i><i></i><i></i><i></i><i></i></div>
<nav class="abs foot-nav"><span>HOME</span><span>|</span><span>ABOUT US</span><span>|</span><span>ATTORNEY PROFILES</span><span>|</span><span>PRACTICE AREAS</span><span>|</span><span>CONTACT US</span></nav>
<div class="abs copy-line">Molaw &copy; 2017 All rights reserved. Terms of use and Privacy Policy</div>

</body>
</html>
```